Professional Modern Website Design

We are a premium IT services provider to the financial industry based in London. Our company is called Veltra our current holding page is www.veltra-example.co.uk. We require a new website to match our new corporate identity. This project is for the design phase only. Development will be handled in-house. I have attached examples of wire frames we have developed (although open to suggestions for improvement) Our brand document that should demonstrate current brand, inc how we communicate to potential clients and finally mostly completed web-content.
We are looking for designers that can create something that sets us apart from our competitors.
Target Market(s)
IT Decision makers in Finance companies such as; hedge funds, private investment banks etc
Industry/Entity Type
Financial
Number of Pages Required
5+ page
Requirements
Must have
- hexagon elements in the design, unique design.
Nice to have
- Blog and social media feeds
Should not have
- Should not resemble a downloaded template

```html
<!DOCTYPE html>
<html lang="en">
<head>
<meta charset="utf-8">
<title>Veltra – IT services for finance</title>
<link href="https://fonts.googleapis.com/css2?family=Raleway:wght@200;300;600&family=Open+Sans:wght@400;600&display=swap" rel="stylesheet">
<style>
:root{
  --orange:#f26a21;
  --orange-dark:#d4551a;
  --ink:#1b1b1b;
  --panel:#232323;
  --hero-a:#2a2a2a;
  --hero-b:#121212;
  --text-light:#e9e9e9;
  --text-muted:#a9a9a9;
  --white:#ffffff;
}
*{box-sizing:border-box;margin:0;padding:0}
html,body{width:758px;height:1200px;overflow:hidden}
body{background:var(--ink);font-family:'Open Sans',sans-serif;color:var(--text-light);position:relative}

.hero{position:absolute;left:0;top:0;width:758px;height:545px;
  background:radial-gradient(ellipse at 30% 70%,#3b3b3b 0%,var(--hero-a) 35%,var(--hero-b) 100%)}
.hero-person{position:absolute;left:455px;top:158px;width:303px;height:387px;
  background:linear-gradient(160deg,#6d6a66 0%,#3d3a38 45%,#1f1f1f 100%)}

.brand{position:absolute;top:22px;left:0;width:758px;text-align:center;display:flex;flex-direction:column;align-items:center;gap:6px}
.brand-mark{width:30px;height:30px;background:var(--orange)}
.brand-name{font-family:'Raleway',sans-serif;font-weight:600;font-size:14px;letter-spacing:3px;color:var(--white)}

.main-nav{position:absolute;left:316px;top:130px;width:442px;height:28px;background:var(--orange);display:flex}
.main-nav a{flex:1;text-align:center;line-height:28px;font-size:10px;color:var(--white);text-decoration:none;letter-spacing:.5px}
.main-nav a.active{background:var(--orange-dark)}

.dropdown{position:absolute;left:400px;top:158px;width:150px;background:var(--orange);padding:6px 0}
.dropdown a{display:block;font-size:9px;color:var(--white);text-decoration:none;padding:0 10px;line-height:34px;border-bottom:1px solid rgba(255,255,255,.25)}
.dropdown a:last-child{border-bottom:none}

.hero-copy{position:absolute;left:88px;top:238px;width:245px}
.hero-copy h1{font-family:'Raleway',sans-serif;font-weight:300;font-size:16px;line-height:21px;text-transform:uppercase;color:var(--white)}
.hero-copy p{font-size:9.5px;line-height:14px;color:var(--text-light);margin-top:8px}
.btn{display:inline-block;margin-top:12px;background:var(--orange);color:var(--white);font-size:11px;padding:4px 14px;text-decoration:none}

.intro{position:absolute;left:0;top:545px;width:758px;height:175px;background:var(--orange);text-align:center}
.intro h2{font-family:'Raleway',sans-serif;font-weight:200;font-size:48px;letter-spacing:2px;color:var(--white);margin-top:36px}
.intro p{font-size:11px;line-height:16px;color:var(--white);width:440px;margin:14px auto 0}

.audiences{position:absolute;left:0;top:720px;width:758px;height:437px;background:var(--panel);display:flex;justify-content:center;gap:22px;padding-top:72px}
.audience{width:150px;text-align:center}
.audience svg{display:block;margin:0 auto}
.audience h3{font-family:'Raleway',sans-serif;font-weight:600;font-size:11px;line-height:14px;color:var(--orange);text-transform:uppercase;margin-top:20px;min-height:28px;display:flex;align-items:center;justify-content:center}
.audience p{font-size:8.5px;line-height:12.5px;color:var(--text-muted);margin-top:8px}

.site-footer{position:absolute;left:0;top:1157px;width:758px;height:43px;background:var(--orange);text-align:center;padding-top:7px}
.footer-nav{display:flex;justify-content:center;gap:10px;font-size:8.5px}
.footer-nav a{color:var(--white);text-decoration:none}
.footer-nav span{color:var(--white)}
.copyright{font-size:8px;color:var(--white);margin-top:5px}
</style>
</head>
<body>

<header class="hero">
  <div class="hero-person" role="img" aria-label="Photo of a businessman in a suit writing at a desk, city skyline behind"></div>

  <div class="brand">
    <span class="brand-mark"></span>
    <span class="brand-name">VELTRA</span>
  </div>

  <nav class="main-nav">
    <a href="#">ABOUT</a>
    <a href="#" class="active">SERVICES</a>
    <a href="#">PARTNERS</a>
    <a href="#">CLIENTS</a>
    <a href="#">CONTACT</a>
  </nav>

  <div class="dropdown">
    <a href="#">Data centre &amp; infrastructure</a>
    <a href="#">Support managed &amp; services</a>
    <a href="#">Voice and data</a>
    <a href="#">Hosting and cloud</a>
    <a href="#">Security and ISP</a>
  </div>

  <div class="hero-copy">
    <h1>You need integration. We're helping there with you.</h1>
    <p>Veltra is one of the leading systems integrators to the world's finance sector. We are an extension of your business and our cross-platform expertise has been built so you always have access to a complete partner.</p>
    <a href="#" class="btn">About Us</a>
  </div>
</header>

<section class="intro">
  <h2>WHO ARE YOU?</h2>
  <p>If you're part of a financial organisation, we have the power to help everyone work more efficiently, productively and profitably.</p>
</section>

<section class="audiences">
  <article class="audience">
    <svg width="140" height="150" viewBox="0 0 140 150"><polygon points="70,3 136,39 136,111 70,147 4,111 4,39" fill="#9a9a9a"/><polygon points="70,9 131,42 131,108 70,141 9,108 9,42" fill="#5b6470" role="img" aria-label="Portrait photo of a senior hedge fund manager"/></svg>
    <h3>Senior Hedge Fund<br>Manager/CEO</h3>
    <p>You need to develop and implement strategy for sustainable growth while ensuring profitability. Your staff are your biggest asset and security is a key concern in an always-on world. Veltra can help you find the best solutions so your business grows at the pace you want.</p>
  </article>
  <article class="audience">
    <svg width="140" height="150" viewBox="0 0 140 150"><polygon points="70,3 136,39 136,111 70,147 4,111 4,39" fill="#9a9a9a"/><polygon points="70,9 131,42 131,108 70,141 9,108 9,42" fill="#8b7e74" role="img" aria-label="Portrait photo of a finance director"/></svg>
    <h3>CFO</h3>
    <p>Your key responsibility is to obtain the maximum return from products and services. You understand investment opportunities and want higher efficiencies from every pound spent. We can help you spend wisely on the right technology, so what your firm needs is delivered while making a measurable return.</p>
  </article>
  <article class="audience">
    <svg width="140" height="150" viewBox="0 0 140 150"><polygon points="70,3 136,39 136,111 70,147 4,111 4,39" fill="#9a9a9a"/><polygon points="70,9 131,42 131,108 70,141 9,108 9,42" fill="#6f7c88" role="img" aria-label="Portrait photo of an IT manager"/></svg>
    <h3>IT Manager/CTO</h3>
    <p>Integration with partners and vendors is your key concern. You want to make sure any IT system you implement will work with the whole infrastructure of your company. Veltra lets you focus on your users while we ensure every platform stays secure, current and ready for the next generation.</p>
  </article>
  <article class="audience">
    <svg width="140" height="150" viewBox="0 0 140 150"><polygon points="70,3 136,39 136,111 70,147 4,111 4,39" fill="#9a9a9a"/><polygon points="70,9 131,42 131,108 70,141 9,108 9,42" fill="#7a7068" role="img" aria-label="Photo of employees working together at a laptop"/></svg>
    <h3>Employee</h3>
    <p>You're working hard, but not getting anywhere fast. You want the tools to make your job easier, so you can spend more time thinking about what you're doing rather than how you're doing it. You shouldn't have to think about technology. Veltra can help you get back on track.</p>
  </article>
</section>

<footer class="site-footer">
  <nav class="footer-nav">
    <a href="#">HOME</a><span>|</span>
    <a href="#">ABOUT</a><span>|</span>
    <a href="#">SERVICES</a><span>|</span>
    <a href="#">PARTNERS</a><span>|</span>
    <a href="#">CLIENTS</a><span>|</span>
    <a href="#">CONTACT</a>
  </nav>
  <p class="copyright">© 2014 www.veltra-example.co.uk - All Rights Reserved</p>
</footer>

</body>
</html>
```